Design a business card & stationary for a mortgage company

We are looking for a good looking business card design for our mortgage company that includes our logo. We received a free design as part of our logo project but we don't love it. The company is called "Birchfield Mortgage Company" so we like waves and lighthouses. The logo should be included. We have a version in both vertical and horizontal that we have provided.

Industry/Entity Type

Finance

Contact Information for Business Card

This should include our new logo file

Requirements
Must have
• 3. The details you'd like on the card - name, title, phone, email, website, address, social media handles etc.
1. Dennis Marlow
Vice President
614-390-2751
Fax 877-402-6158
dmarlow@birchfieldmortgage.example
NMLS 47192 - Company NMLS 62304
18 Elm Ave
Toms River, NJ 08512

```html
<!DOCTYPE html>
<html lang="en">
<head>
<meta charset="utf-8">
<title>Birchfield Mortgage Company – Business Card</title>
<link rel="stylesheet" href="https://fonts.googleapis.com/css2?family=Josefin+Sans:wght@400&family=Roboto:wght@400;700;900&display=swap">
<style>
  :root {
    --navy: #165a97;
    --navy-deep: #124f86;
    --sky: #1d8fdb;
    --paper: #ffffff;
    --ink: #3c3c3c;
    --backdrop: #e7eaee;
  }
  * { box-sizing: border-box; margin: 0; padding: 0; }
  html, body {
    width: 1200px; height: 900px; overflow: hidden;
    background: var(--backdrop);
    font-family: "Roboto", Arial, sans-serif;
  }
  .card {
    position: absolute; left: 250px;
    width: 700px; height: 400px;
    border-radius: 3px;
    box-shadow: 0 6px 18px rgba(0,0,0,.18);
    overflow: hidden;
  }
  /* back side */
  .card--back { top: 35px; background: var(--navy); }
  .back-brand {
    position: absolute; left: 0; right: 0; top: 105px;
    display: flex; flex-direction: column; align-items: center;
    color: var(--paper); text-align: center;
  }
  .brand-mark {
    width: 58px; height: 58px; border-radius: 50%;
    background: var(--sky); margin-bottom: 18px;
  }
  .back-brand .brand-name {
    font-family: "Josefin Sans", sans-serif;
    font-size: 40px; line-height: 1.15; letter-spacing: 2px; font-weight: 400;
  }
  .back-brand .brand-license {
    margin-top: 14px; font-size: 14px; letter-spacing: 4px; font-weight: 700;
  }
  /* front side */
  .card--front { top: 465px; background: var(--paper); }
  .card-waves { position: absolute; left: 0; top: 0; }
  .front-brand {
    position: absolute; left: 20px; top: 78px; width: 305px;
    display: flex; flex-direction: column; align-items: center;
    text-align: center;
  }
  .front-brand .brand-mark { background: var(--navy); width: 62px; height: 62px; margin-bottom: 16px; }
  .front-brand .brand-name {
    color: var(--navy);
    font-family: "Josefin Sans", sans-serif;
    font-size: 31px; line-height: 1.15; letter-spacing: 1px; font-weight: 400;
  }
  .divider {
    position: absolute; left: 338px; top: 70px; width: 2px; height: 200px;
    background: var(--navy);
  }
  .contact {
    position: absolute; left: 358px; top: 72px; width: 322px; color: var(--ink);
  }
  .contact .person-name {
    color: var(--navy); font-weight: 900; font-size: 25px; letter-spacing: .5px;
  }
  .contact .person-title { font-size: 16px; margin-top: 2px; }
  .contact .license, .contact .address { font-size: 15px; line-height: 1.3; }
  .contact .license { margin-top: 14px; }
  .contact-list { list-style: none; margin-top: 12px; font-size: 15px; line-height: 1.4; }
  .contact-list li { display: flex; align-items: center; gap: 7px; white-space: nowrap; }
  .contact-list svg { width: 14px; height: 14px; fill: var(--navy); flex: none; }
  .website {
    position: absolute; right: 40px; bottom: 14px;
    color: var(--paper); font-size: 18px; letter-spacing: .3px;
  }
</style>
</head>
<body>

<section class="card card--back" aria-label="Business card back">
  <div class="back-brand">
    <span class="brand-mark"></span>
    <div class="brand-name">Birchfield<br>Mortgage Company</div>
    <div class="brand-license">NMLS 62304</div>
  </div>
</section>

<section class="card card--front" aria-label="Business card front">
  <svg class="card-waves" width="700" height="400" viewBox="0 0 700 400" aria-hidden="true">
    <path d="M0,285 C150,350 320,360 460,335 C570,318 650,322 700,336 L700,400 L0,400 Z" fill="var(--sky)"/>
    <path d="M0,297 C150,360 320,368 460,343 C570,326 650,330 700,344 L700,400 L0,400 Z" fill="var(--paper)"/>
    <path d="M0,303 C150,366 320,374 460,349 C570,332 650,336 700,350 L700,400 L0,400 Z" fill="var(--navy)"/>
  </svg>

  <div class="front-brand">
    <span class="brand-mark"></span>
    <div class="brand-name">Birchfield<br>Mortgage Company</div>
  </div>

  <div class="divider"></div>

  <div class="contact">
    <div class="person-name">DENNIS MARLOW</div>
    <div class="person-title">Vice President</div>
    <p class="license">NMLS 47192 - Company NMLS 62304</p>
    <p class="address">18 Elm Ave, Toms River, NJ 08512</p>
    <ul class="contact-list">
      <li>
        <svg viewBox="0 0 24 24"><path d="M6.6 10.8a15.1 15.1 0 0 0 6.6 6.6l2.2-2.2c.3-.3.7-.4 1-.2 1.1.4 2.3.6 3.6.6.6 0 1 .4 1 1V20c0 .6-.4 1-1 1A17 17 0 0 1 3 4c0-.6.4-1 1-1h3.5c.6 0 1 .4 1 1 0 1.3.2 2.5.6 3.6.1.3 0 .7-.2 1z"/></svg>
        614-390-2751
      </li>
      <li>
        <svg viewBox="0 0 24 24"><path d="M6 2h12v5H6zM4 8h16a2 2 0 0 1 2 2v6h-4v6H6v-6H2v-6a2 2 0 0 1 2-2zm4 8v4h8v-4z"/></svg>
        877-402-6158
      </li>
      <li>
        <svg viewBox="0 0 24 24"><path d="M2 5h20v2l-10 6L2 7zm0 4 10 6 10-6v10H2z"/></svg>
        dmarlow@birchfieldmortgage.example
      </li>
    </ul>
  </div>

  <div class="website">www.birchfieldmortgage.example</div>
</section>

</body>
</html>
```